Professional and modern website for Real Estate services company

Hi there! We're looking for a responsive, highly professional and modern (in line with Latest trends) coded website for a Real Estate services company named Portalia (find logo attached). I will try to Explain how I picture it in my head, but feel free to step out of the script and design it as you please. The structure for the website must be as Follows: - Menu: at the top of the screen, always visible (in any page and when to scrolling down). Logo at the left hand side (clicking redirects to home), then a Services, About us, Blog and Contact and on the right hand, Estimate and Log in (just placeholder, no log in required yet). - Home: (I like https://fr.velmora.example/): a landscape picture of Madrid's skyline. Very important That at a first glance (without scrolling) you can see a box to input data of your building to get an estimate (Post code, Number of homes, Number of garages, Number of stores, Swimming pool (yes / no) Concierge (yes / no)). Should there be a small space Also for a corporate presentation video (more or less like https://www.bravunecasales.example/ but With the estimate Request box INSTEAD OF the App - however, do not take this one as example Given I just wanted to illustrate the structure). Still in the Home, bellow the first glance, I'd like to have a brief introduction of the following pages (Services, About us, Blog and Contact). This can be in a Either "square" form (like https://fr.velmora.example/) or in a "scroll" form (like https://k7portales.example/). - Services: we offer 3 sets of services, each of them composed by three specific services, Namely: * Administration Treasury Accounting Savings * Consulting Legal Technical Regulatory * Mediation Repairs Meetings Delinquency For the sake of structuring, each of the nine services will Have to written description composed of 3 small paragraphs of About 15 words. I Tend to like to Accompany With each of the services related icons / vectors, but feel free to design them as you want. - About us: content not yet defined, but will be a series of bullets / sections in Which We talk about prep or differentiating points. We can include the corporate video presentation here again. - Blog: just a space Where you can see to the blog entries (in Home, probably just show 3/4). - Contact: a fancy contact form, with map, address, telephone, e-mail and opening hours. Just to give it a bit more content, maybe include a catch phrase like "We're looking forward to meeting you!" or something like that. - Estimate: this is the Most Important page in the website (in Addition to the upper part of the Home page). Basically replicate the estimate for the home box, but maybe with a bit more design or extended, Given this is a single page just for that. - Log in: opens a drop-down with user and password (just placeholder, no log in required yet). Regarding colors, we still do not Have a color scheme, so anything in line With the logo is OK. Many thanks in advance, Martin

Target Market(s)

All ages and genders

Industry/Entity Type

Real Estate

Coding

Coded - Design and coding required

Number of Pages Required

5+ page

Font styles to use
Sans Serif

Requirements
Must have
• Blank colored background

```html
<!DOCTYPE html>
<html lang="en">
<head>
<meta charset="utf-8">
<title>Portalia — Home Owners' Association Management</title>
<link rel="stylesheet" href="https://fonts.googleapis.com/css2?family=Catamaran:wght@400;500;600;700;800&family=Open+Sans:ital,wght@0,400;0,600;0,700;1,400&display=swap">
<style>
:root{
  --orange:#d6780c;
  --orange-overlay:#d98624;
  --ink:#1c1c1c;
  --text:#555;
  --light-bg:#ebebeb;
  --card:#f4f4f4;
  --footer:#1a1a1a;
  --footer-bottom:#111;
  --footer-text:#cfcfcf;
  --button-grey:#4a4a4a;
  --white:#fff;
}
*{box-sizing:border-box;margin:0;padding:0}
html,body{width:1200px;height:3056px;overflow:hidden}
body{font-family:"Open Sans",Arial,sans-serif;color:var(--text);background:var(--white);position:relative}
h1,h2,h3,h4{font-family:"Catamaran","Open Sans",sans-serif}

/* Header */
.site-header{position:absolute;top:0;left:0;width:1200px;height:138px;background:var(--white)}
.brand{position:absolute;left:62px;top:40px;display:flex;align-items:center;gap:10px;font-family:"Catamaran",sans-serif;font-weight:700;font-size:40px;line-height:1;color:#3b3b3b}
.brand-mark{width:14px;height:14px;background:var(--orange)}
.social-top{position:absolute;right:62px;top:22px;display:flex;gap:6px}
.social-top span{width:32px;height:32px;border-radius:50%;background:#111;display:block}
.main-nav{position:absolute;right:58px;top:78px;display:flex;align-items:center}
.main-nav a{font-family:"Catamaran",sans-serif;font-weight:600;font-size:16px;color:#111;text-decoration:none;padding:8px 15px;letter-spacing:.3px}
.main-nav a.active{background:var(--orange);color:var(--white)}

/* Hero */
.hero{position:absolute;top:138px;left:0;width:1200px;height:532px;background:linear-gradient(180deg,#8fb2d6 0%,#c9d8e6 35%,#9aa6ad 62%,#6d6a5e 82%,#5c5040 100%)}
.estimate{position:absolute;left:145px;top:178px;width:920px}
.estimate-tag{display:inline-block;background:rgba(214,120,12,.85);color:var(--white);font-family:"Catamaran",sans-serif;font-weight:600;font-size:21px;padding:8px 16px;width:342px}
.estimate-box{background:rgba(214,120,12,.85);padding:22px 18px;display:flex;gap:10px;align-items:center}
.estimate-box input{height:40px;border:1px solid #ddd;background:var(--white);font-family:"Open Sans",sans-serif;font-size:13px;padding:0 14px;color:#888;width:176px}
.estimate-box button{height:40px;width:114px;background:#000;color:var(--white);border:0;font-family:"Open Sans",sans-serif;font-weight:600;font-size:17px;margin-left:2px}

/* Intro */
.intro{position:absolute;top:670px;left:0;width:1200px;height:290px;text-align:center}
.intro p{margin-top:66px;font-size:24px;color:#222;font-family:"Catamaran",sans-serif;font-weight:500}
.intro h2{font-size:38px;font-weight:800;color:var(--orange);letter-spacing:.5px;margin-top:2px}
.btn-ask{display:inline-block;margin-top:10px;background:var(--button-grey);color:var(--white);font-size:16px;padding:11px 22px;text-decoration:none}

/* Services */
.services{position:absolute;top:960px;left:0;width:1200px;height:738px;background:linear-gradient(135deg,#e0913a 0%,var(--orange-overlay) 45%,#c8700f 100%);color:var(--white)}
.services-head{text-align:center;padding-top:70px}
.services-head h2{font-size:42px;font-weight:700;letter-spacing:.5px;line-height:1}
.services-head p{font-size:13px;margin-top:10px}
.service{position:absolute;width:290px}
.service-icon{width:86px;height:86px;border:3px solid var(--white);border-radius:50%;display:flex;align-items:center;justify-content:center;margin-bottom:8px}
.service h3{font-size:24px;font-weight:700;line-height:1.1}
.service p{font-size:13px;line-height:1.3;margin-top:4px}

/* Testimonials */
.testimonials{position:absolute;top:1698px;left:0;width:1200px;height:308px;background:var(--light-bg)}
.quote{position:absolute;top:84px;width:508px;height:153px;background:var(--white);padding:28px 44px 0 44px}
.quote-avatar{position:absolute;top:-36px;left:34px;width:66px;height:66px;border-radius:50%;background:linear-gradient(180deg,#9a6a52,#e8cfc0);border:4px solid var(--white)}
.quote p{font-size:13px;line-height:1.7;color:#666}
.quote p .mark{color:var(--orange);font-family:Georgia,serif;font-size:26px;font-weight:700;line-height:0;vertical-align:-6px;margin-right:6px}
.quote cite{display:block;margin-top:12px;font-style:normal;font-size:12px;font-weight:700;color:#555}
.quote cite em{font-weight:400;color:#777}

/* Blog */
.blog{position:absolute;top:2006px;left:0;width:1200px;height:660px}
.blog h2{text-align:center;font-size:40px;font-weight:700;color:#111;margin-top:74px;letter-spacing:.5px}
.post{position:absolute;top:184px;width:320px;height:413px;background:var(--card)}
.post-image{height:210px}
.post-date{position:absolute;top:180px;left:17px;width:60px;height:60px;border-radius:50%;background:var(--orange);color:var(--white);text-align:center;font-family:"Catamaran",sans-serif;line-height:1}
.post-date b{display:block;font-size:24px;font-weight:700;margin-top:9px}
.post-date span{font-size:13px;font-weight:600}
.post-body{padding:38px 18px 0 18px}
.post-body h3{font-family:"Open Sans",sans-serif;font-size:14.5px;font-weight:400;color:#222;line-height:1.25}
.post-meta{display:flex;gap:18px;margin-top:8px;font-size:13px;color:#999;align-items:center}
.post-meta span{display:flex;align-items:center;gap:5px}
.post-body p{font-size:11.5px;line-height:1.65;color:#555;margin-top:12px}

/* Footer */
.site-footer{position:absolute;top:2666px;left:0;width:1200px;height:338px;background:var(--footer);color:var(--footer-text)}
.footer-col{position:absolute;top:40px}
.footer-brand{font-family:"Catamaran",sans-serif;font-weight:700;font-size:30px;line-height:1;color:var(--white);display:flex;align-items:center;gap:8px}
.footer-brand i{width:10px;height:10px;background:var(--white);display:block}
.contact-line{display:flex;align-items:center;gap:12px;font-size:12.5px;margin-top:22px}
.contact-line:first-of-type{margin-top:28px}
.footer-social{display:flex;gap:10px;margin-top:24px}
.footer-social span{width:30px;height:30px;border-radius:50%;border:1px solid #555;display:block}
.footer-col h4{font-size:16px;font-weight:700;color:var(--white);letter-spacing:.3px;margin-bottom:22px}
.news-item{font-size:12px;color:#ddd;margin-bottom:14px}
.news-item small{display:block;font-size:9px;color:#aaa;margin-top:4px}
.about-text{font-size:11.5px;line-height:2;color:#ccc;width:240px}
.field{width:234px;height:36px;background:#2b2b2b;color:#bbb;font-size:10.5px;padding:11px 12px;margin-bottom:12px}
.field.message{height:92px}
.footer-bottom{position:absolute;top:3004px;left:0;width:1200px;height:52px;background:var(--footer-bottom);color:#888;font-size:12px;text-align:center;line-height:52px}
</style>
</head>
<body>

<header class="site-header">
  <div class="brand"><span class="brand-mark"></span>Portalia</div>
  <div class="social-top" aria-label="Social links"><span></span><span></span><span></span><span></span></div>
  <nav class="main-nav">
    <a class="active" href="#">HOME</a>
    <a href="#">ABOUT US</a>
    <a href="#">SERVICES</a>
    <a href="#">RATES</a>
    <a href="#">BLOG</a>
    <a href="#">RESOURCES</a>
    <a href="#">CONTACT</a>
  </nav>
</header>

<section class="hero" role="img" aria-label="City skyline with skyscrapers under a cloudy blue sky">
  <form class="estimate">
    <div class="estimate-tag">We offer what you can afford</div>
    <div class="estimate-box">
      <input type="text" placeholder="Post code">
      <input type="text" placeholder="Number of homes">
      <input type="text" placeholder="Number of garages">
      <input type="text" placeholder="Swimming pool (yes/no)">
      <button type="button">Submit</button>
    </div>
  </form>
</section>

<section class="intro">
  <p>Effective management of your home owners' association</p>
  <h2>EFFECTIVE RESOURCES</h2>
  <a class="btn-ask" href="#">Ask Your Question Today</a>
</section>

<section class="services" role="img" aria-label="Orange-toned photo of people reviewing documents at a desk">
  <div class="services-head">
    <h2>OUR SERVICES</h2>
    <p>We Make Mortgages Easy we working for you not for bank</p>
  </div>

  <div class="service" style="left:63px;top:240px">
    <div class="service-icon"><svg width="40" height="40" viewBox="0 0 40 40" fill="none" stroke="#fff" stroke-width="3"><circle cx="16" cy="12" r="7"/><path d="M3 36c0-8 6-13 13-13"/><circle cx="29" cy="29" r="7"/></svg></div>
    <h3>Administration</h3>
    <p>Learn what you can afford and find your maximum mortgage.Learn what you can afford and find your maximum mortgage</p>
  </div>
  <div class="service" style="left:473px;top:240px">
    <div class="service-icon"><svg width="40" height="40" viewBox="0 0 40 40" fill="none" stroke="#fff" stroke-width="3"><path d="M6 18L20 6l14 12v16H6z"/><path d="M20 16v12M14 22h12"/></svg></div>
    <h3>Consulting</h3>
    <p>Learn what you can afford and find your maximum mortgage.Learn what you can afford and find your maximum mortgage</p>
  </div>
  <div class="service" style="left:864px;top:240px">
    <div class="service-icon"><svg width="40" height="40" viewBox="0 0 40 40" fill="#fff"><circle cx="12" cy="16" r="5"/><circle cx="28" cy="16" r="5"/><path d="M3 34c0-6 4-10 9-10s9 4 9 10zM19 34c0-6 4-10 9-10s9 4 9 10z"/><circle cx="20" cy="7" r="4"/></svg></div>
    <h3>Mediation</h3>
    <p>Learn what you can afford and find your maximum mortgage.Learn what you can afford and find your maximum mortgage</p>
  </div>

  <div class="service" style="left:63px;top:478px">
    <div class="service-icon"><svg width="40" height="40" viewBox="0 0 40 40" fill="none" stroke="#fff" stroke-width="3"><path d="M14 8h12l-3 6h-6zM11 34c-4 0-5-4-4-8 2-6 6-10 13-10s11 4 13 10c1 4 0 8-4 8z"/><path d="M20 20v10M17 23h6M17 28h6"/></svg></div>
    <h3>Legal Consulting</h3>
    <p>Learn what you can afford and find your maximum mortgage.Learn what you can afford and find your maximum mortgage</p>
  </div>
  <div class="service" style="left:473px;top:478px">
    <div class="service-icon"><svg width="40" height="40" viewBox="0 0 40 40" fill="none" stroke="#fff" stroke-width="3"><circle cx="20" cy="10" r="5"/><path d="M13 24c0-4 3-7 7-7s7 3 7 7z" fill="#fff"/><path d="M4 22c2 8 8 12 16 12s14-4 16-12"/></svg></div>
    <h3>Meetings</h3>
    <p>Learn what you can afford and find your maximum mortgage.Learn what you can afford and find your maximum mortgage</p>
  </div>
  <div class="service" style="left:874px;top:478px">
    <div class="service-icon"><svg width="40" height="40" viewBox="0 0 40 40"><circle cx="20" cy="20" r="15" fill="#fff"/><path d="M13 20l5 5 9-10" fill="none" stroke="#d98624" stroke-width="4"/></svg></div>
    <h3>Savings</h3>
    <p>Learn what you can afford and find your maximum mortgage.Learn what you can afford and find your maximum mortgage</p>
  </div>
</section>

<section class="testimonials">
  <blockquote class="quote" style="left:81px">
    <div class="quote-avatar" role="img" aria-label="Portrait of the client"></div>
    <p><span class="mark">“</span>Aenean dictum varius odio et suscipit. Morbi vulputate metus condimentum, accumsan erat vitae, scelerisque libero. Integer id dictum velit. Suspendisse eget commodo.</p>
    <cite>Nora L. Vidal, <em>School Teacher</em></cite>
  </blockquote>
  <blockquote class="quote" style="left:609px">
    <div class="quote-avatar" role="img" aria-label="Portrait of the client"></div>
    <p><span class="mark">“</span>Aenean dictum varius odio et suscipit. Morbi vulputate metus condimentum, accumsan erat vitae, scelerisque libero. Integer id dictum velit. Suspendisse eget commodo.</p>
    <cite>Nora L. Vidal, <em>School Teacher</em></cite>
  </blockquote>
</section>

<section class="blog">
  <h2>LATEST BLOG POSTS</h2>

  <article class="post" style="left:61px">
    <div class="post-image" role="img" aria-label="Woman sorting paperwork at a kitchen table" style="background:linear-gradient(160deg,#e8e6e0,#8aa0b8 55%,#c9b49a)"></div>
    <div class="post-date"><b>18</b><span>APR</span></div>
    <div class="post-body">
      <h3>International group limited complete asset acquisition</h3>
      <div class="post-meta">
        <span><svg width="11" height="11" viewBox="0 0 11 11" fill="#aaa"><circle cx="5.5" cy="3" r="2.6"/><path d="M0 11c0-3 2.5-5 5.5-5s5.5 2 5.5 5z"/></svg>By admin</span>
        <span><svg width="12" height="11" viewBox="0 0 12 11" fill="#aaa"><rect x="0" y="4" width="3" height="7"/><path d="M4 4l3-4c1 0 2 1 1.5 2L8 4h3.5l-1 7H4z"/></svg>10</span>
        <span><svg width="14" height="11" viewBox="0 0 14 11" fill="#aaa"><path d="M1 0h12v8H5l-3 3V8H1z"/></svg>20</span>
      </div>
      <p>Global microfiber expert to stabilize and focus growth of Ostrava based advanced wound care company...</p>
    </div>
  </article>

  <article class="post" style="left:440px">
    <div class="post-image" role="img" aria-label="Calculator and house-shaped paper cutout on a wooden desk" style="background:linear-gradient(160deg,#6e4a30,#a9a79c 55%,#7a5236)"></div>
    <div class="post-date"><b>15</b><span>JAN</span></div>
    <div class="post-body">
      <h3 style="width:230px">To transition to new  to new ownership</h3>
      <div class="post-meta">
        <span><svg width="11" height="11" viewBox="0 0 11 11" fill="#aaa"><circle cx="5.5" cy="3" r="2.6"/><path d="M0 11c0-3 2.5-5 5.5-5s5.5 2 5.5 5z"/></svg>By admin</span>
        <span><svg width="12" height="11" viewBox="0 0 12 11" fill="#aaa"><rect x="0" y="4" width="3" height="7"/><path d="M4 4l3-4c1 0 2 1 1.5 2L8 4h3.5l-1 7H4z"/></svg>10</span>
        <span><svg width="14" height="11" viewBox="0 0 14 11" fill="#aaa"><path d="M1 0h12v8H5l-3 3V8H1z"/></svg>20</span>
      </div>
      <p>Company to be acquired and reorganized under new ownership</p>
    </div>
  </article>

  <article class="post" style="left:819px">
    <div class="post-image" role="img" aria-label="People signing documents at a bright office table" style="background:linear-gradient(160deg,#b8c2cc,#eef0f2 55%,#9aa0a8)"></div>
    <div class="post-date"><b>6</b><span>MAY</span></div>
    <div class="post-body">
      <h3>Collaboration between Tarvo and Ilsu is awarded addition NRF grant with</h3>
      <div class="post-meta">
        <span><svg width="11" height="11" viewBox="0 0 11 11" fill="#aaa"><circle cx="5.5" cy="3" r="2.6"/><path d="M0 11c0-3 2.5-5 5.5-5s5.5 2 5.5 5z"/></svg>By admin</span>
        <span><svg width="12" height="11" viewBox="0 0 12 11" fill="#aaa"><rect x="0" y="4" width="3" height="7"/><path d="M4 4l3-4c1 0 2 1 1.5 2L8 4h3.5l-1 7H4z"/></svg>10</span>
        <span><svg width="14" height="11" viewBox="0 0 14 11" fill="#aaa"><path d="M1 0h12v8H5l-3 3V8H1z"/></svg>20</span>
      </div>
      <p>collaboration between Tarvo and Ilsu is awarded addition NRF grant with total value of $1.1M for the developement of a....</p>
    </div>
  </article>
</section>

<footer class="site-footer">
  <div class="footer-col" style="left:69px">
    <div class="footer-brand">Portalia<i></i></div>
    <div class="contact-line"><svg width="14" height="14" viewBox="0 0 14 14" fill="#ddd"><path d="M3 0l3 3-2 2c1 2 3 4 5 5l2-2 3 3-2 3C6 14 0 8 0 3z"/></svg>(800) 555 72 00</div>
    <div class="contact-line"><svg width="14" height="12" viewBox="0 0 14 12" fill="none" stroke="#ddd" stroke-width="1.5"><rect x="1" y="1" width="12" height="10"/><path d="M1 1l6 5 6-5"/></svg>hello@portalia.example</div>
    <div class="contact-line"><svg width="12" height="15" viewBox="0 0 12 15" fill="#ddd"><path d="M6 0a6 6 0 016 6c0 4-6 9-6 9S0 10 0 6a6 6 0 016-6z"/><circle cx="6" cy="6" r="2" fill="#1a1a1a"/></svg>48 Calle Arbolera, Madrid,<br>28014, Spain</div>
    <div class="footer-social"><span></span><span></span><span></span><span></span><span></span><span></span></div>
  </div>

  <div class="footer-col" style="left:371px">
    <h4>LATEST NEWS</h4>
    <div class="news-item">This is a Audio post Type<small>January 5, 2016</small></div>
    <div class="news-item">This is a Gallery post Type<small>January 5, 2016</small></div>
    <div class="news-item">This is a Quote post Type<small>January 5, 2016</small></div>
    <div class="news-item">Post Video<small>October 3, 2015</small></div>
  </div>

  <div class="footer-col" style="left:601px">
    <h4>ABOUT</h4>
    <p class="about-text">Cum sociis natoque penatibus et magnis dis parturient montes, nascetur ridiculus mus. Etiam imperdiet. Ut sollicitudin sem sit amet ipsum. In id dui. Pellentesque sapien. Curabitur commodo elit eget erat. Aliquam sit amet nibh. Ut vitae elit. Donec ac nisi eget.</p>
  </div>

  <div class="footer-col" style="left:882px">
    <h4>QUICK CONTACT</h4>
    <div class="field">YOUR NAME</div>
    <div class="field">YOUR EMAIL</div>
    <div class="field message">MESSAGE...</div>
  </div>
</footer>

<div class="footer-bottom">Copyright © 2016 Portalia. All Rights Reserved.</div>

</body>
</html>
```